Best-selling business author needs Next Craft Line book cover designs

We're launching a series of books and online training videos badged under the "Brightfork Notes - Next Craft Line" brand. The idea is that there are titles for each of the future skills that people will need to survive the robots in the future, eg, Creativity, Critical Thinking Skills, Problem Solving, etc. The exciting job here is to create a series thematic look, and a specific design for the first title, Sharp Prompts.
Hope my brief challenges you, and look forward to your questions and designs.

Target Market(s)

start ups and corporate market (mainly in Asia Pacific) looking to upskill themselves. Probably 18-45 age group, including uni business students, and people working in Meridian 400s.

Industry/Entity Type

Publishing Company

Font styles to use
Serif
Sans Serif
Other font styles liked:
• Felt marker or other 'handcrafted' styles because these will be 'workbook' style publications

Colors
ec1f27
3276b5
00a990
9bcb3c
fbed22
f78f20
6b449b

Requirements
Must have
• Must look professional but not boring or old school.
• Use the "Brightfork Notes Next Craft Line" (logo attached).
• Need category, ie "critical thinking" associated with logo above
• Need title and subtitle of the book, ie "SHARP PROMPTS. How to shape better questions to create explosive breakthroughs."
• All the type you see on sample design, ie reviewers blurb at top, author's name etc.
• Vivid and strong colour schemes to be eye -catching individually but especially strong when lined up on bookshelves together.
• See examples attached for QTV series (competitor) and also a quick design hack by myself to give an idea of what it "might" look like.
• A5 portrait format.
• Spine and Back page will be largely text (with barcode, see example).
• Back page text:
• Heading: Ways to Win the Modern Market with Bold Inquiry Habits.
• - Find out the Sharp Prompts that kick-started empires like NestLoop, Colby Hensel, Beanrowe, Vitalume, Sky Orin, Melodex, Zentrix, Orbely, Tobin Wexley, and even Fundquill.
• - Learn how companies like R&T, Quince, Varlo, AeroMint, Fablon, Lyra, Caravel R3, Movra, and Tulp use Sharp Prompts to develop blockbuster new products, experiences and marketing messages.
• - How to identify and eradicate your cognitive blindspots.
• - How to create a Curiosity Gap (and why that’s so important).
• - Why it’s important to challenge the Status Quo, and how to do it.
• Heading: What if there was a formula for creating Sharp Prompts? There is!
• Get on board this rocket ship with business creativity expert (and best-selling author) Reg Mannix as he guides you through a proven system for creating more insightful, more powerful questions, which point us toward breakthrough solutions, products, and process innovations.
• For the first time, he shares the Sharp Prompts (Discovery Prompt Building Method) here. The same system that he has taught to senior executives from major corporations such as Norvale Bank, Strivon, KessmarFahr, Medwyn, Tolvax, and many other progressive companies.
• Heading: Praise for Sharp Prompts
• “Really enjoyed Sharp Prompts. Like taking a peek into the minds of some of the greatest innovators right as they were asking these SHARP PROMPTS that prompted them to create history!” Rohan Dutt, Head of R&D, Quartel China.
• “Awesome! It’s a great book, I’m a huge fan of the power of questions.” Gavin Hoskins, VP, Norvale Bank.
• "Sharp Prompts is a Sharp Book! This has really helped with both my classroom sessions and consulting projects. Well done!"
• Martin Esterhal, Adj. Professor, The University of Bramcote.
• www.regmannix.example #sharp prompts
• [insert bar code]
Nice to have
• Prefer simple strong bold graphic approach.
• Using photos, or icons to highlight the topic. Please avoid cliches.
Should not have
• Not overly fancy, ornate, or visually complicated.

```html
<!DOCTYPE html>
<html lang="en">
<head>
<meta charset="utf-8">
<title>Sharp Prompts – Book Cover</title>
<link rel="stylesheet" href="https://fonts.googleapis.com/css2?family=Bebas+Neue&family=Archivo+Black&family=Open+Sans:wght@400&family=Roboto+Slab:wght@400&display=swap">
<style>
  :root {
    --stage: #e3e4e0;
    --orange: #f0922c;
    --red: #e8262c;
    --yellow: #f5ec1f;
    --white: #ffffff;
    --ink: #1c1c1c;
    --steel: #5f6163;
    --steel-light: #8d9093;
    --tag-grey: #c9cdd2;
  }
  * { margin: 0; padding: 0; box-sizing: border-box; }
  html, body {
    width: 1200px; height: 1200px; overflow: hidden;
    background: var(--stage);
  }
  .cover {
    position: absolute; left: 205px; top: 37px;
    width: 790px; height: 1125px;
    background: var(--red);
    overflow: hidden;
    font-family: "Bebas Neue", "Oswald", sans-serif;
  }
  .cover__band {
    position: absolute; left: 0; top: 0; width: 100%; height: 327px;
    background: var(--orange);
  }
  .blurb {
    position: absolute; left: 60px; top: 14px; width: 660px;
    text-align: center; color: var(--ink);
    font-size: 29px; line-height: 37px; letter-spacing: -0.2px;
  }
  .series-badge {
    position: absolute; left: 0; top: 147px; width: 287px; height: 93px;
    background: var(--white);
    display: flex; align-items: center; gap: 10px; padding-left: 12px;
  }
  .series-badge__mark { width: 26px; height: 26px; background: var(--red); flex: none; }
  .series-badge__name {
    font-family: "Open Sans", sans-serif; font-size: 27px; color: var(--ink); line-height: 1;
  }
  .series-badge__line {
    font-family: "Roboto Slab", serif; font-size: 13px; color: var(--ink);
    letter-spacing: 0.5px; margin-top: 5px;
  }
  .category {
    position: absolute; left: 0; top: 244px;
    font-size: 52px; line-height: 52px; color: var(--ink);
  }
  .hero-art {
    position: absolute; left: 590px; top: 132px; width: 185px; height: 362px;
    border-radius: 92px 92px 60px 60px;
    background: linear-gradient(160deg, var(--steel-light), var(--steel));
  }
  .title {
    position: absolute; line-height: 1; display: block; white-space: nowrap;
  }
  .title--first { top: 362px; left: 195px; font-size: 183px; color: var(--yellow); }
  .title--second { top: 494px; left: 0; width: 100%; text-align: center; padding-left: 14px; font-size: 183px; color: var(--white); }
  .subtitle {
    position: absolute; left: 40px; top: 652px; width: 740px;
    text-align: center; color: var(--yellow);
    font-size: 63px; line-height: 77px;
  }
  .author {
    position: absolute; left: 0; top: 942px; width: 100%; text-align: center;
    font-family: "Archivo Black", sans-serif; font-size: 36px; color: var(--white);
  }
  .author-roles {
    position: absolute; left: 0; top: 996px; width: 100%; text-align: center;
    font-family: "Open Sans", sans-serif; font-size: 33px; color: var(--tag-grey);
  }
  .author-roles .sep { color: var(--ink); margin: 0 6px; }
</style>
</head>
<body>
  <main class="cover">
    <div class="cover__band"></div>

    <p class="blurb">“More stimulation than a double shot of cold brew infused<br>coffee. Full of energy, fresh and bright ideas.”<br>Tomas Vrell, Fellow, Kestrel Micro.</p>

    <div class="series-badge">
      <span class="series-badge__mark"></span>
      <div>
        <div class="series-badge__name">Brightfork Notes</div>
        <div class="series-badge__line">NEXT CRAFT LINE &gt;&gt;&gt;</div>
      </div>
    </div>
    <p class="category">Critical Thinking</p>

    <div class="hero-art" role="img" aria-label="Large grey 3D question mark whose dot is a lit round bomb"></div>

    <h1>
      <span class="title title--first">SHARP</span>
      <span class="title title--second">PROMPTS</span>
    </h1>

    <p class="subtitle">“How to shape better questions<br>to create explosive<br>breakthroughs”</p>

    <p class="author">Reg Mannix</p>
    <p class="author-roles">TalkStage MC<span class="sep">|</span>Storyteller<span class="sep">|</span>Firebrand</p>
  </main>
</body>
</html>
```